Business Card for innovative, tech/consultant company

We are specializing in bringing together Efficiency methodology and Technology for our Business customers. We would like an astonishing business Card that matches this idea.

Target Market(s)

Businesses of medium size or more

Industry/Entity Type

Business Consultant

Contact Information for Business Card

Name, Title, personal email, www, address, phone

Font styles to use
Sans Serif

Colors
3277b5

Requirements
Must have
• - innovative, efficient design
• - good readable
• - Colors must match our logo (blue and grey)
• - the attached font (is licensed by our Company) must be used (Syntax LT)
Should not have
• overloaded

```html
<!DOCTYPE html>
<html lang="en">
<head>
<meta charset="utf-8">
<title>Veloxa Business Card</title>
<link rel="stylesheet" href="https://fonts.googleapis.com/css2?family=Montserrat:wght@400;500;700&display=swap">
<style>
  :root {
    --page-bg: #e4e6e9;
    --card-bg: #f5f6f7;
    --brand-blue: #1d5c9a;
    --name-blue: #1f5a93;
    --logo-grey: #58595b;
    --text-grey: #4a4b4d;
    --bar-grey: #4d4e50;
    --divider-blue: #1d5c9a;
  }
  html, body {
    margin: 0;
    padding: 0;
    width: 1200px;
    height: 970px;
    overflow: hidden;
    background: var(--page-bg);
    font-family: "Montserrat", sans-serif;
  }
  .card {
    position: absolute;
    left: 100px;
    top: 206px;
    width: 1000px;
    height: 557px;
    background: var(--card-bg);
    border-radius: 26px;
    overflow: hidden;
    box-shadow: 0 10px 30px rgba(0,0,0,0.12);
    color: var(--text-grey);
  }
  .brand-name {
    position: absolute;
    left: 58px;
    top: 40px;
    margin: 0;
    font-size: 170px;
    font-weight: 500;
    line-height: 1;
    letter-spacing: -4px;
    color: var(--logo-grey);
  }
  .name-tab {
    position: absolute;
    left: 0;
    top: 288px;
    width: 13px;
    height: 82px;
    background: var(--brand-blue);
    border-radius: 0 6px 6px 0;
  }
  .person-name {
    position: absolute;
    left: 50px;
    top: 298px;
    margin: 0;
    font-size: 35px;
    font-weight: 700;
    color: var(--name-blue);
    line-height: 1.1;
  }
  .person-title {
    position: absolute;
    left: 51px;
    top: 340px;
    margin: 0;
    font-size: 24px;
    font-weight: 400;
    color: var(--text-grey);
  }
  .contact-block {
    position: absolute;
    top: 418px;
    font-size: 24px;
    line-height: 35px;
    margin: 0;
  }
  .address { left: 50px; }
  .phones { left: 398px; }
  .web { left: 718px; }
  .contact-line {
    display: flex;
    align-items: center;
    gap: 10px;
    white-space: nowrap;
  }
  .contact-icon { width: 22px; height: 22px; flex: none; }
  .divider {
    position: absolute;
    top: 426px;
    width: 3px;
    height: 54px;
    background: var(--divider-blue);
  }
  .divider-one { left: 345px; }
  .divider-two { left: 657px; }
  .footer-bars {
    position: absolute;
    left: 0;
    bottom: 0;
    width: 1000px;
    height: 35px;
  }
  .bar { position: absolute; top: 0; height: 35px; }
  .bar-left { left: 0; width: 265px; background: var(--bar-grey); }
  .bar-middle { left: 269px; width: 465px; background: var(--brand-blue); }
  .bar-right { left: 739px; width: 261px; background: var(--bar-grey); }
</style>
</head>
<body>
  <section class="card">
    <h1 class="brand-name">Veloxa</h1>

    <div class="name-tab"></div>
    <h2 class="person-name">Daniel Mercer</h2>
    <p class="person-title">Owner / Founder</p>

    <address class="contact-block address" style="font-style:normal">
      <div class="contact-line">214 Larkspur Road,</div>
      <div class="contact-line">Fairbrook, 40512</div>
    </address>

    <div class="divider divider-one"></div>

    <div class="contact-block phones">
      <div class="contact-line">
        <svg class="contact-icon" viewBox="0 0 24 24" aria-hidden="true">
          <rect x="7" y="2.5" width="10" height="19" rx="2" fill="none" stroke="var(--brand-blue)" stroke-width="2"/>
          <circle cx="12" cy="18" r="1.2" fill="var(--brand-blue)"/>
        </svg>
        <span>+ 000 000 0000</span>
      </div>
      <div class="contact-line">
        <svg class="contact-icon" viewBox="0 0 24 24" aria-hidden="true">
          <path d="M3 9c0-3 4-5 9-5s9 2 9 5v1.5h-4.5V8.5h-9v2H3z" fill="var(--brand-blue)"/>
          <rect x="5" y="11" width="14" height="9" rx="2" fill="var(--brand-blue)"/>
          <circle cx="12" cy="15.5" r="2.4" fill="var(--card-bg)"/>
        </svg>
        <span>+ 000 000 0000</span>
      </div>
    </div>

    <div class="divider divider-two"></div>

    <div class="contact-block web">
      <div class="contact-line">
        <svg class="contact-icon" viewBox="0 0 24 24" aria-hidden="true">
          <rect x="2.5" y="5.5" width="19" height="13" rx="1.5" fill="var(--brand-blue)"/>
          <path d="M3.5 6.5l8.5 6.5 8.5-6.5" fill="none" stroke="var(--card-bg)" stroke-width="1.6"/>
        </svg>
        <span>info@veloxa.co.uk</span>
      </div>
      <div class="contact-line">
        <svg class="contact-icon" viewBox="0 0 24 24" aria-hidden="true">
          <rect x="2.5" y="4" width="19" height="12.5" rx="1" fill="none" stroke="var(--brand-blue)" stroke-width="2.2"/>
          <rect x="9" y="17" width="6" height="2.5" fill="var(--brand-blue)"/>
          <rect x="6.5" y="19.5" width="11" height="1.8" fill="var(--brand-blue)"/>
        </svg>
        <span>www.veloxa.co.uk</span>
      </div>
    </div>

    <div class="footer-bars">
      <div class="bar bar-left"></div>
      <div class="bar bar-middle"></div>
      <div class="bar bar-right"></div>
    </div>
  </section>
</body>
</html>
```